Investment Firm Needs a Business Card Design

Need a business card for a new professional services firm that provides financial planning and investment management. Design should communicate financial safety and innovation. The contact information that needs to be on card is under Must Haves.

Target Market(s)

Retail Public

Industry/Entity Type

Investment

Requirements
Must have
• The data that needs to appear is in quotations:
"Darren Whitcombe, RWA"
(RWA logo either below my name or near my name)

"4417 Marlowe Lane
Suite 305
St. Charles, IL 60389"

"800-547-3162" (office)
"630-924-7318" (cell)
"darren@ledgerbeacon.net" (email)
"www.LedgerBeacon.net"
Nice to have
• would like to have the tag line "Steady Horizon(r)" with registered trade mark somewhere on card, maybe on back.

```html
<!DOCTYPE html>
<html lang="en">
<head>
<meta charset="utf-8">
<title>Ledger Beacon Business Card</title>
<link rel="stylesheet" href="https://fonts.googleapis.com/css2?family=Open+Sans:wght@400;600;700&display=swap">
<style>
  :root {
    --navy: #2b3270;
    --green: #3aa14a;
    --ink: #2a2a2a;
    --rule: #4a4a4a;
    --paper: #ffffff;
    --backdrop: #e9e9eb;
  }
  * { margin: 0; padding: 0; box-sizing: border-box; }
  html, body {
    width: 1200px;
    height: 1005px;
    overflow: hidden;
    background: var(--backdrop);
    font-family: "Open Sans", Arial, sans-serif;
  }
  .card {
    position: absolute;
    left: 220px;
    width: 760px;
    height: 434px;
    background: var(--paper);
    box-shadow: 0 4px 14px rgba(0,0,0,0.12);
    overflow: hidden;
  }
  .card--back { top: 50px; }
  .card--front { top: 521px; }

  .brand-square {
    position: absolute;
    background: var(--navy);
  }
  .brand-name {
    position: absolute;
    font-weight: 700;
    letter-spacing: 2px;
    text-transform: uppercase;
    color: var(--navy);
    white-space: nowrap;
    line-height: 1;
  }
  .divider {
    position: absolute;
    width: 2px;
    background: var(--rule);
  }

  /* back */
  .card--back .brand-square { left: 270px; top: 100px; width: 80px; height: 80px; }
  .card--back .brand-name { left: 120px; top: 200px; font-size: 40px; }
  .card--back .divider { left: 640px; top: 90px; height: 250px; }

  /* front */
  .side-band {
    position: absolute;
    left: 48px; top: 0;
    width: 16px; height: 100%;
    background: var(--navy);
  }
  .card--front .brand-square { left: 112px; top: 56px; width: 80px; height: 80px; }
  .card--front .divider { left: 222px; top: 46px; height: 120px; }
  .card--front .brand-name { left: 250px; top: 130px; font-size: 34px; }

  .contact {
    position: absolute;
    left: 100px;
    top: 212px;
    color: var(--ink);
  }
  .contact__name {
    font-size: 24px;
    font-weight: 700;
    color: var(--green);
    margin-bottom: 8px;
    white-space: nowrap;
  }
  .contact__name span { color: var(--ink); }
  .contact__row {
    display: flex;
    align-items: center;
    gap: 12px;
    font-size: 18px;
    line-height: 32px;
    white-space: nowrap;
  }
  .contact__icon { width: 16px; height: 16px; fill: var(--ink); flex: none; }
</style>
</head>
<body>

<section class="card card--back">
  <div class="brand-square"></div>
  <div class="brand-name">Ledger Beacon</div>
  <div class="divider"></div>
</section>

<section class="card card--front">
  <div class="side-band"></div>
  <div class="brand-square"></div>
  <div class="divider"></div>
  <div class="brand-name">Ledger Beacon</div>

  <div class="contact">
    <p class="contact__name">Darren <span>Whitcombe, RWA</span></p>
    <p class="contact__row">
      <svg class="contact__icon" viewBox="0 0 16 16" aria-hidden="true"><path d="M8 1a5 5 0 0 1 5 5c0 4-5 9-5 9S3 10 3 6a5 5 0 0 1 5-5z"/><circle cx="8" cy="6" r="2" fill="#fff"/></svg>
      4417 Marlowe Lane, Suite 305, St. Charles, IL 60389
    </p>
    <p class="contact__row">
      <svg class="contact__icon" viewBox="0 0 16 16" aria-hidden="true"><path d="M4 1h3l1 4-2 1.5c.8 1.8 2 3 3.5 3.5L11 8l4 1v3c0 1.5-1 2.5-2.5 2.5C6.5 14.5 1.5 9.5 1.5 3.5 1.5 2 2.5 1 4 1z"/></svg>
      800-547-3162 (office) &nbsp;·&nbsp; 630-924-7318 (cell)
    </p>
    <p class="contact__row">
      <svg class="contact__icon" viewBox="0 0 16 16" aria-hidden="true"><path d="M1 3h14v10H1z M1 3l7 6 7-6" stroke="#fff" stroke-width="1"/></svg>
      darren@ledgerbeacon.net
    </p>
    <p class="contact__row">
      <svg class="contact__icon" viewBox="0 0 16 16" aria-hidden="true"><circle cx="8" cy="8" r="7"/><path d="M1 8h14M8 1c3 3 3 11 0 14M8 1c-3 3-3 11 0 14" stroke="#fff" stroke-width="1" fill="none"/></svg>
      www.LedgerBeacon.net
    </p>
  </div>
</section>

</body>
</html>
```